Graffiti removal company needs cool flyer

Beacon Rinse & Spray is a pressure washing company based in Alberta, Canada - we offer general power washing and graffiti removal services for residential & commercial properties. . We would like an edgy/cool 2 sided flyer created to hand out to business / possible door hanger style with specific focus on graffiti removal but also touching on the power washing we can provide. The flyer should have the added pictures (use some before & afters) & wording attached. The picture from Harlow Dome should be used as its a prominent sports arena. There should be some graffiti fonts used to convey the titles/ steps/headings but the look should be clean.
Contact info to appear on flyer
Company logo
Ph 780-555-0143
derek@beaconrinse.ca
www.beaconrinseandspray.ca

```html
<!DOCTYPE html>
<html lang="en">
<head>
<meta charset="utf-8">
<title>Beacon Rinse &amp; Spray – Graffiti Removal Door Hanger</title>
<link rel="stylesheet" href="https://fonts.googleapis.com/css2?family=Permanent+Marker&family=Poppins:wght@400;500;600;700&display=block">
<style>
  :root {
    --navy: #0c2a52;
    --navy-deep: #081d3b;
    --orange: #f26a21;
    --grey: #8b8e92;
    --grey-light: #f1f1f1;
    --ink: #1e2a3a;
    --stage: #e3e3e3;
    --white: #ffffff;
  }
  * { box-sizing: border-box; margin: 0; padding: 0; }
  html, body { width: 1200px; height: 2303px; overflow: hidden; background: var(--stage); }
  body { font-family: "Poppins", sans-serif; color: var(--ink); position: relative; }

  .hanger {
    position: absolute; top: 514px; width: 520px; height: 1274px;
    background: var(--white); overflow: hidden;
    box-shadow: 0 12px 30px rgba(0,0,0,.18);
  }
  .hanger--front { left: 40px; }
  .hanger--back { left: 640px; }
  .hanger-cut { position: absolute; inset: 0; width: 520px; height: 260px; z-index: 5; }

  .brand-plate {
    position: absolute; left: 83px; top: 236px; width: 352px; height: 101px;
    background: rgba(12,42,82,.82); border-radius: 14px;
    display: flex; align-items: center; justify-content: center; gap: 14px; z-index: 3;
  }
  .brand-mark { width: 22px; height: 22px; border-radius: 50%; background: var(--white); flex: none; }
  .brand-name { color: var(--white); font-weight: 600; font-size: 25px; line-height: 1.1; letter-spacing: 1px; text-transform: uppercase; }

  .photo { position: absolute; left: 0; width: 520px; }
  .photo--arena { top: 0; height: 587px; background: linear-gradient(180deg, #d9dcdf 0%, #a9b2ba 45%, #6f7a84 75%, #4b535b 100%); }
  .chevron { position: absolute; left: 0; top: 440px; width: 520px; height: 147px; z-index: 2; }

  .why { position: absolute; top: 606px; left: 40px; right: 40px; text-align: center; }
  .why h2 { color: var(--navy); font-size: 17.5px; font-weight: 600; margin-bottom: 6px; }
  .why p { font-size: 13px; line-height: 1.38; color: #333; }

  .pill { background: var(--navy); color: var(--white); border-radius: 30px; display: inline-block; text-align: center; }
  .steps-title { position: absolute; left: 110px; top: 751px; width: 296px; height: 44px; font-size: 29px; font-weight: 500; line-height: 44px; }

  .steps-rail { position: absolute; left: 69px; top: 773px; width: 41px; height: 240px; border-left: 2px solid #9da0a4; border-top: 2px solid #9da0a4; border-top-left-radius: 14px; }
  .step { position: absolute; left: 43px; right: 46px; display: flex; align-items: center; gap: 18px; }
  .step-icon { position: relative; width: 52px; height: 52px; border-radius: 50%; background: var(--grey); flex: none; display: flex; align-items: center; justify-content: center; }
  .step-num { position: absolute; left: -3px; top: -3px; width: 17px; height: 17px; border-radius: 50%; background: var(--orange); color: var(--white); font-size: 10px; font-weight: 600; text-align: center; line-height: 17px; }
  .step p { font-size: 12px; line-height: 1.45; color: #333; }
  .step p strong { font-weight: 600; }
  .step--one { top: 810px; }
  .step--two { top: 884px; }
  .step--three { top: 992px; }
  .divider { position: absolute; left: 110px; right: 46px; border-top: 1.5px dashed #9da0a4; }
  .divider--a { top: 870px; }
  .divider--b { top: 979px; }

  .closing { position: absolute; left: 0; top: 1065px; width: 520px; height: 149px; background: var(--grey-light); text-align: center; padding: 18px 44px 0; }
  .closing p { font-size: 12.5px; line-height: 1.42; color: #333; }
  .closing p.closing-call { color: var(--ink); font-size: 14.5px; font-weight: 500; margin-top: 10px; line-height: 1.55; }

  .contact-bar { position: absolute; left: 0; bottom: 0; width: 520px; height: 60px; background: var(--navy); }
  .contact-phone { position: absolute; left: 20px; top: 0; height: 60px; display: flex; align-items: center; gap: 8px; color: var(--white); font-size: 30px; font-weight: 600; }
  .contact-web { position: absolute; right: 0; top: 0; width: 245px; height: 60px; background: var(--grey); clip-path: polygon(14px 0, 100% 0, 100% 100%, 0 100%); color: var(--white); font-size: 15px; text-align: right; padding: 6px 20px 0 0; line-height: 1.45; }

  .hanger--back .sky { position: absolute; left: 0; top: 0; width: 520px; height: 820px; background: linear-gradient(180deg, var(--navy) 0%, #163a68 32%, #4a5d74 50%, #7b6c63 70%, #8a5b4a 100%); }
  .hanger--back .brand-plate { background: none; top: 236px; }
  .title { position: absolute; left: 0; width: 520px; text-align: center; font-family: "Permanent Marker", "Poppins", sans-serif; line-height: 1; z-index: 2; }
  .title--graffiti { top: 340px; color: var(--orange); font-size: 86px; letter-spacing: 1px; }
  .title--removal { top: 448px; color: var(--white); font-size: 74px; }
  .chevron--back { top: 700px; height: 180px; }

  .ba-circle { position: absolute; top: 672px; width: 178px; height: 178px; border-radius: 50%; border: 4px solid var(--white); z-index: 3; overflow: hidden; }
  .ba-circle--before { left: 63px; background: linear-gradient(160deg, #d8d4cf 0%, #a8543f 55%, #c23030 80%, #7a4a3a 100%); }
  .ba-circle--after { left: 278px; background: linear-gradient(160deg, #c9cdd1 0%, #b06b4f 50%, #8e8f92 80%, #6b5045 100%); }
  .ba-label { position: absolute; top: 818px; width: 108px; height: 30px; line-height: 30px; font-size: 16px; font-weight: 600; z-index: 4; }
  .ba-label--before { left: 98px; }
  .ba-label--after { left: 313px; }
  .ba-arrow { position: absolute; left: 214px; top: 826px; width: 90px; height: 40px; z-index: 4; }

  .info { position: absolute; left: 36px; right: 36px; text-align: center; z-index: 4; }
  .info .pill { font-size: 16px; font-weight: 600; height: 26px; line-height: 26px; padding: 0 22px; margin-bottom: 5px; letter-spacing: .3px; }
  .info p { font-size: 12.5px; line-height: 1.42; color: #333; }
  .info--trusted { top: 880px; }
  .info--response { top: 978px; }
  .info--about { top: 1110px; }
</style>
</head>
<body>

<section class="hanger hanger--front">
  <div class="photo photo--arena" role="img" aria-label="Photo of the Harlow Dome sports arena with a Beacon Rinse &amp; Spray service truck parked in front"></div>
  <svg class="chevron" viewBox="0 0 520 147" aria-hidden="true">
    <polygon points="0,26 262,147 0,147" fill="#0c2a52"/>
    <polygon points="520,20 258,147 520,147" fill="#0c2a52"/>
    <polygon points="120,147 260,82 400,147" fill="#ffffff"/>
  </svg>
  <div class="brand-plate"><span class="brand-mark"></span><span class="brand-name">Beacon<br>Rinse &amp; Spray</span></div>

  <div class="why">
    <h2>Why is it important to remove graffiti quickly?</h2>
    <p>Graffiti tags are often viewed as ‘calling cards’ for the vandals that leave them. Simply put – one tag will encourage another, and another, and another to the same area. The best way to prevent graffiti is to quickly remove it. Removing it will also put you in compliance with Edmonton’s Community Standards Bylaw 14600 .</p>
  </div>

  <div class="steps-rail"></div>
  <div class="pill steps-title">EASY AS 1, 2, 3</div>

  <div class="step step--one">
    <div class="step-icon"><span class="step-num">1</span>
      <svg width="24" height="24" viewBox="0 0 24 24" aria-hidden="true"><path d="M6.6 10.8a15 15 0 0 0 6.6 6.6l2.2-2.2a1 1 0 0 1 1-.25 11.4 11.4 0 0 0 3.6.57 1 1 0 0 1 1 1V20a1 1 0 0 1-1 1A17 17 0 0 1 3 4a1 1 0 0 1 1-1h3.5a1 1 0 0 1 1 1 11.4 11.4 0 0 0 .57 3.6 1 1 0 0 1-.25 1z" fill="#fff"/></svg>
    </div>
    <p>Call for a free quote - <strong>780-555-0143</strong></p>
  </div>
  <div class="divider divider--a"></div>
  <div class="step step--two">
    <div class="step-icon"><span class="step-num">2</span>
      <svg width="26" height="26" viewBox="0 0 26 26" aria-hidden="true"><circle cx="14" cy="11" r="7" fill="none" stroke="#fff" stroke-width="2"/><path d="M9 16l-5 5" stroke="#fff" stroke-width="3" stroke-linecap="round"/><path d="M11 11l2 2 4-4" fill="none" stroke="#fff" stroke-width="2"/></svg>
    </div>
    <p>Beacon Rinse &amp; Spray arrives within 24 hrs to Identify the tag (examine the substrate &amp; surface ), provide quote, schedule removal of graffiti with eco-friendly biodegradable solutions &amp; pressure wash the area clean.</p>
  </div>
  <div class="divider divider--b"></div>
  <div class="step step--three">
    <div class="step-icon"><span class="step-num">3</span>
      <svg width="26" height="24" viewBox="0 0 26 24" aria-hidden="true"><rect x="3" y="4" width="20" height="16" rx="2" fill="none" stroke="#fff" stroke-width="2"/><path d="M5 18l6-6 4 4 3-3 4 5z" fill="#fff"/><circle cx="17" cy="9" r="2" fill="#fff"/></svg>
    </div>
    <p>Provide before and after photos documenting the removal of the graffiti.</p>
  </div>

  <div class="closing">
    <p>Studies have shown the best strategy for the prevention of further graffiti is immediate removal. The longer graffiti lingers, the more graffiti and vandalism it attracts.</p>
    <p class="closing-call">No matter what’s been put on your property it won’t be there for long when you Call Beacon Rinse &amp; Spray.</p>
  </div>

  <div class="contact-bar">
    <div class="contact-phone">
      <svg width="22" height="22" viewBox="0 0 24 24" aria-hidden="true"><path d="M6.6 10.8a15 15 0 0 0 6.6 6.6l2.2-2.2a1 1 0 0 1 1-.25 11.4 11.4 0 0 0 3.6.57 1 1 0 0 1 1 1V20a1 1 0 0 1-1 1A17 17 0 0 1 3 4a1 1 0 0 1 1-1h3.5a1 1 0 0 1 1 1 11.4 11.4 0 0 0 .57 3.6 1 1 0 0 1-.25 1z" fill="#f26a21"/></svg>
      780-555-0143
    </div>
    <div class="contact-web">beaconrinseandspray.ca<br>derek@beaconrinse.ca</div>
  </div>

  <svg class="hanger-cut" viewBox="0 0 520 260" aria-hidden="true">
    <path d="M0,95 C70,100 150,112 215,108 L215,178 C150,150 70,132 0,128 Z" fill="#e3e3e3"/>
    <circle cx="269" cy="152" r="70" fill="#e3e3e3"/>
  </svg>
</section>

<section class="hanger hanger--back">
  <div class="sky" role="img" aria-label="Photo of a technician in hi-vis gear steam cleaning graffiti off a brick wall"></div>
  <div class="brand-plate"><span class="brand-mark"></span><span class="brand-name">Beacon<br>Rinse &amp; Spray</span></div>
  <div class="title title--graffiti">GRAFFITI</div>
  <div class="title title--removal">REMOVAL</div>

  <svg class="chevron chevron--back" viewBox="0 0 520 180" aria-hidden="true">
    <polygon points="0,10 0,180 250,180" fill="#0c2a52"/>
    <polygon points="520,0 520,180 270,180" fill="#0c2a52"/>
    <polygon points="0,120 0,180 520,180 520,120 260,80" fill="#ffffff"/>
  </svg>

  <div class="ba-circle ba-circle--before" role="img" aria-label="Before: brick wall covered in red graffiti"></div>
  <div class="ba-circle ba-circle--after" role="img" aria-label="After: the same brick wall cleaned"></div>
  <div class="pill ba-label ba-label--before">Before</div>
  <div class="pill ba-label ba-label--after">After</div>
  <svg class="ba-arrow" viewBox="0 0 90 40" aria-hidden="true">
    <path d="M6,12 Q40,42 78,16" fill="none" stroke="#8b8e92" stroke-width="3"/>
    <path d="M68,12 L82,13 L76,25" fill="none" stroke="#8b8e92" stroke-width="3"/>
  </svg>

  <div class="info info--trusted">
    <div class="pill">TRUSTED</div>
    <p>Beacon Rinse &amp; Spray provides commercial graffiti removal services in the City of Edmonton &amp; Surrounding areas . We provide effective removal solutions for businesses affected by graffiti vandalism.</p>
  </div>
  <div class="info info--response">
    <div class="pill">QUICK RESPONSE</div>
    <p>We are here to help! Once we receive your call, Our team will arrange a site visit within 24 hrs to assess the surface, quote for the service, and then remove the graffiti. Beacon is committed to helping your business maintain a clean and professional property appearance. Your image matters to us!</p>
  </div>
  <div class="info info--about">
    <div class="pill">ABOUT US</div>
    <p>We have been in business since 2011, providing power washing &amp; graffiti removal cleaning solutions. We are one of the largest Power washing companies within Edmonton!</p>
  </div>

  <div class="contact-bar">
    <div class="contact-phone">
      <svg width="22" height="22" viewBox="0 0 24 24" aria-hidden="true"><path d="M6.6 10.8a15 15 0 0 0 6.6 6.6l2.2-2.2a1 1 0 0 1 1-.25 11.4 11.4 0 0 0 3.6.57 1 1 0 0 1 1 1V20a1 1 0 0 1-1 1A17 17 0 0 1 3 4a1 1 0 0 1 1-1h3.5a1 1 0 0 1 1 1 11.4 11.4 0 0 0 .57 3.6 1 1 0 0 1-.25 1z" fill="#f26a21"/></svg>
      780-555-0143
    </div>
    <div class="contact-web">beaconrinseandspray.ca<br>derek@beaconrinse.ca</div>
  </div>

  <svg class="hanger-cut" viewBox="0 0 520 260" aria-hidden="true">
    <path d="M300,115 C370,100 440,78 520,70 L520,160 C440,168 370,180 300,190 Z" fill="#e3e3e3"/>
    <circle cx="265" cy="152" r="70" fill="#e3e3e3"/>
  </svg>
</section>

</body>
</html>
```